Vornel Technologies business card design

We need a business card designed with our new logo. it would be great if the card could communicate it is a technology based company.

Target Market(s)

system integrators

Industry/Entity Type

technology, IOT

Contact Information for Business Card

Name, designation, Address, telephone number, email address

Requirements
Must have
• logo and company name
Nice to have
• something to do with technology

```html
<!DOCTYPE html>
<html lang="en">
<head>
<meta charset="utf-8">
<title>Vornel Technologies – Business Card</title>
<link href="https://fonts.googleapis.com/css2?family=Lexend:wght@200;300;600&display=swap" rel="stylesheet">
<style>
  :root {
    --page: #ffffff;
    --card-top: #222222;
    --card-bottom: #363636;
    --shade: #1e1f1f;
    --ink: #ffffff;
    --accent: #f7941d;
  }
  * { margin: 0; padding: 0; box-sizing: border-box; }
  html, body { width: 1200px; height: 1200px; overflow: hidden; background: var(--page); }
  .canvas { position: relative; width: 1200px; height: 1200px; }
  .card {
    position: absolute; left: 174px; width: 850px; height: 508px; overflow: hidden;
    background: linear-gradient(160deg, var(--card-top) 0%, var(--card-bottom) 100%);
  }
  .card--front { top: 89px; }
  .card--back { top: 608px; height: 509px; }
  .card__shapes { position: absolute; inset: 0; width: 100%; height: 100%; }
  .card__pattern { position: absolute; inset: 0; background: linear-gradient(135deg, rgba(255,255,255,0.02), rgba(255,255,255,0.05)); }
  .brand { position: absolute; display: flex; align-items: center; gap: 18px; font-family: "Lexend", sans-serif; font-weight: 600; color: var(--ink); }
  .brand__mark { background: var(--accent); flex: none; }
  .brand__name { display: flex; flex-direction: column; line-height: 1; }
  .brand__word { letter-spacing: 0.02em; }
  .brand__sub { letter-spacing: 0.42em; }
  .card--front .brand { left: 208px; top: 186px; }
  .card--front .brand__mark { width: 62px; height: 62px; }
  .card--front .brand__word { font-size: 68px; }
  .card--front .brand__sub { font-size: 22px; margin-top: 12px; }
  .card--back .brand { left: 490px; top: 202px; gap: 12px; }
  .card--back .brand__mark { width: 40px; height: 40px; }
  .card--back .brand__word { font-size: 42px; }
  .card--back .brand__sub { font-size: 13.5px; margin-top: 8px; }
  .contact { position: absolute; left: 80px; top: 160px; list-style: none; font-family: "Lexend", sans-serif; font-weight: 200; color: var(--ink); }
  .contact__item { display: flex; align-items: center; height: 64px; }
  .contact__icon { width: 36px; height: 36px; flex: none; margin-right: 9px; fill: var(--ink); }
  .contact__text { font-size: 25px; letter-spacing: -0.02em; padding-bottom: 4px; border-bottom: 2.5px solid var(--accent); border-radius: 2px; line-height: 1.1; }
</style>
</head>
<body>
<div class="canvas">
  <section class="card card--front">
    <div class="card__pattern" role="img" aria-label="Faint circuit-trace pattern in dark grey"></div>
    <svg class="card__shapes" viewBox="0 0 850 508" aria-hidden="true">
      <path d="M0,71 A203,203 0 0 1 0,439 Z" fill="var(--shade)" opacity="0.85"/>
      <path d="M850,71 A203,203 0 0 0 850,439 Z" fill="var(--shade)" opacity="0.85"/>
    </svg>
    <div class="brand">
      <span class="brand__mark"></span>
      <div class="brand__name"><span class="brand__word">VORNEL</span><span class="brand__sub">TECHNOLOGIES</span></div>
    </div>
  </section>

  <section class="card card--back">
    <div class="card__pattern" role="img" aria-label="Faint circuit-trace pattern in dark grey"></div>
    <svg class="card__shapes" viewBox="0 0 850 509" aria-hidden="true">
      <path d="M383,0 L850,0 L850,509 L726,509 C560,500 462,390 435,254 Z" fill="var(--shade)" opacity="0.85"/>
    </svg>
    <ul class="contact">
      <li class="contact__item">
        <svg class="contact__icon" viewBox="0 0 36 36"><path d="M18 2a12 12 0 0 0-12 12c0 6 8 16 12 20 4-4 12-14 12-20A12 12 0 0 0 18 2zm0 7a5 5 0 1 1 0 10 5 5 0 0 1 0-10z" fill-rule="evenodd"/></svg>
        <span class="contact__text">214 Harlow Street</span>
      </li>
      <li class="contact__item">
        <svg class="contact__icon" viewBox="0 0 36 36"><circle cx="18" cy="18" r="16" fill="none" stroke="#fff" stroke-width="3"/><ellipse cx="18" cy="18" rx="7" ry="16" fill="none" stroke="#fff" stroke-width="3"/><path d="M2 18h32" stroke="#fff" stroke-width="3"/></svg>
        <span class="contact__text">www.vornelnet.com</span>
      </li>
      <li class="contact__item">
        <svg class="contact__icon" viewBox="0 0 36 36"><rect x="2" y="6" width="32" height="24" rx="3" fill="none" stroke="#fff" stroke-width="2.5"/><path d="M3 7l15 13L33 7z"/></svg>
        <span class="contact__text">hello@vornelnet.com</span>
      </li>
      <li class="contact__item">
        <svg class="contact__icon" viewBox="0 0 36 36"><path d="M8 3c3-1 4 4 3 7-1 2 5 10 9 10 2-1 6-1 7 2 1 3-3 5-6 3C15 23 8 16 6 10 5 7 5 4 8 3z"/></svg>
        <span class="contact__text">0317 482 650</span>
      </li>
    </ul>
    <div class="brand">
      <span class="brand__mark"></span>
      <div class="brand__name"><span class="brand__word">VORNEL</span><span class="brand__sub">TECHNOLOGIES</span></div>
    </div>
  </section>
</div>
</body>
</html>
```